We need a fresh, new church business card!!

We need a church business card with basic info to hand out as invites. We are looking for something clean that communicates our basic information clearly.

We are open to square or rectangle card sizes.

General Public

Religious

The attached logo is the only one that I have available. We'd like to see options with with text of the logo lighter and on a dark background as well as options with white/light backgrounds.

Also, we'd like to see option with rounded corners.

• Address - 2718 Maple Row, Lindell, OR 97999
• Website - brookvane.example
• Phone - 555-555-0163
• Service times -
• Sunday - 10am Sunday School
• - 11am Family Worship
• - 6pm Night of Prayer
• Wednesday - 7:30pm Adult Bible Study
• Classes for all ages

```html
<!DOCTYPE html>
<html lang="en">
<head>
<meta charset="utf-8">
<title>Brookvane Pentecostal Church – Business Card</title>
<link rel="stylesheet" href="https://fonts.googleapis.com/css2?family=EB+Garamond:wght@400;600&family=Josefin+Sans:wght@400;600&display=swap">
<style>
  :root {
    --backdrop: #1d1d1f;
    --paper: #f7f8f8;
    --slate: #6d6e70;
    --teal: #3f8593;
    --ink: #555759;
    --ink-light: #e6e6e6;
  }
  * { box-sizing: border-box; margin: 0; padding: 0; }
  html, body { width: 1200px; height: 873px; overflow: hidden; background: var(--backdrop); }
  .stage {
    width: 1200px; height: 873px;
    display: flex; align-items: center; justify-content: center; gap: 40px;
  }
  .card {
    position: relative; width: 540px; height: 309px;
    overflow: hidden; background: var(--slate);
  }
  .card-bg { position: absolute; inset: 0; }
  .wordmark {
    position: absolute; display: flex; align-items: center; gap: 14px;
    font-family: "Josefin Sans", sans-serif; font-weight: 400; color: var(--ink);
  }
  .wordmark-dot { width: 44px; height: 44px; border-radius: 50%; background: var(--teal); flex: none; }
  .wordmark-name { font-size: 34px; letter-spacing: 2px; line-height: 1; text-transform: uppercase; white-space: nowrap; }
  .wordmark-sub { display: block; font-size: 13px; letter-spacing: 5.4px; margin-top: 4px; }
  .front .wordmark { left: 62px; top: 92px; }
  .front .website {
    position: absolute; right: 40px; bottom: 30px;
    font-family: "EB Garamond", serif; font-size: 17px; letter-spacing: 2px; color: var(--ink-light);
  }
  .back .wordmark { left: 150px; top: 40px; }
  .back .wordmark-dot { width: 38px; height: 38px; }
  .back .wordmark-name { font-size: 29px; }
  .back .wordmark-sub { font-size: 11px; letter-spacing: 4.6px; }
  .schedule {
    position: absolute; left: 30px; top: 178px;
    font-family: "EB Garamond", serif; color: var(--ink-light); font-size: 15px; line-height: 19px;
    white-space: nowrap;
  }
  .schedule-title { font-weight: 600; font-size: 17px; text-decoration: underline; letter-spacing: .5px; }
  .schedule b { font-weight: 600; }
  .schedule-note { margin-top: 6px; font-size: 17px; letter-spacing: .5px; }
  .contact {
    position: absolute; left: 290px; top: 172px; list-style: none;
    font-family: "EB Garamond", serif; color: var(--ink-light); font-size: 14px;
  }
  .contact li { display: flex; align-items: center; gap: 10px; margin-bottom: 10px; white-space: nowrap; }
  .contact svg { flex: none; }
</style>
</head>
<body>
<main class="stage">

  <section class="card front" aria-label="Card front">
    <svg class="card-bg" viewBox="0 0 540 309" aria-hidden="true">
      <rect width="540" height="309" fill="var(--slate)"/>
      <path d="M0,0 H540 V62 C480,100 430,205 300,232 C200,252 90,222 0,258 Z" fill="var(--teal)"/>
      <path d="M0,0 H540 V48 C470,86 420,192 300,218 C200,238 90,208 0,244 Z" fill="var(--paper)"/>
    </svg>
    <div class="wordmark">
      <span class="wordmark-dot"></span>
      <span class="wordmark-name">Brookvane<span class="wordmark-sub">Pentecostal Church</span></span>
    </div>
    <p class="website">www.brookvane.example</p>
  </section>

  <section class="card back" aria-label="Card back">
    <svg class="card-bg" viewBox="0 0 540 309" aria-hidden="true">
      <rect width="540" height="309" fill="var(--slate)"/>
      <path d="M0,0 H540 V70 C500,110 420,132 300,140 C190,148 80,146 0,180 Z" fill="var(--teal)"/>
      <path d="M0,0 H540 V56 C500,96 420,118 300,126 C190,134 80,132 0,166 Z" fill="var(--paper)"/>
    </svg>
    <div class="wordmark">
      <span class="wordmark-dot"></span>
      <span class="wordmark-name">Brookvane<span class="wordmark-sub">Pentecostal Church</span></span>
    </div>
    <div class="schedule">
      <p class="schedule-title">SERVICE TIMES:</p>
      <p>Sunday - 10:00am Sunday School</p>
      <p><b>11:00am:</b> Family Worship</p>
      <p><b>06:00pm:</b> Night of Prayer</p>
      <p>Wednesday - 7:30pm Adult Bible Study</p>
      <p class="schedule-note">CLASSES FOR ALL AGES</p>
    </div>
    <ul class="contact">
      <li>
        <svg width="12" height="18" viewBox="0 0 12 18" aria-hidden="true"><rect x="1" y="1" width="10" height="16" rx="2" fill="none" stroke="var(--ink-light)" stroke-width="1.4"/><line x1="4.5" y1="14" x2="7.5" y2="14" stroke="var(--ink-light)" stroke-width="1.2"/></svg>
        <span>555-555-0163</span>
      </li>
      <li>
        <svg width="16" height="12" viewBox="0 0 16 12" aria-hidden="true"><rect x="1" y="1" width="14" height="10" fill="none" stroke="var(--ink-light)" stroke-width="1.3"/><path d="M1,1 L8,7 L15,1" fill="none" stroke="var(--ink-light)" stroke-width="1.3"/></svg>
        <span>2718 Maple Row, Lindell, OR 97999</span>
      </li>
    </ul>
  </section>

</main>
</body>
</html>
```